Sales and Lettings Boards

Hello, please see attached our sales and lettings boards for our estate agency. These were "designed" by the sign writers. As you can see they are pretty flat and boring - could you work your magic and make them stand out please? I've also attached the logo files. Many thanks, Dean

Target Market(s)

Consumers - residential sale property sales and lettings

Industry/Entity Type

Real Estate Agent

```html
<!DOCTYPE html>
<html lang="en">
<head>
<meta charset="utf-8">
<title>Haven Sales &amp; Letting – For Sale Board</title>
<link href="https://fonts.googleapis.com/css2?family=Montserrat:wght@600;700&display=swap" rel="stylesheet">
<style>
  :root {
    --paper: #ffffff;
    --board: #4d4d4f;
    --green: #63b946;
    --ink-light: #ffffff;
  }
  * { margin: 0; padding: 0; box-sizing: border-box; }
  html, body {
    width: 1200px;
    height: 1000px;
    overflow: hidden;
    background: var(--paper);
    font-family: "Montserrat", Arial, sans-serif;
  }
  .canvas {
    position: relative;
    width: 1200px;
    height: 1000px;
    background: var(--paper);
  }
  .board {
    position: absolute;
    left: 97px;
    top: 97px;
    width: 1006px;
    height: 805px;
    background: var(--board);
  }
  .brand-name {
    position: absolute;
    left: 54px;
    top: 16px;
    font-weight: 700;
    font-size: 208px;
    line-height: 1;
    letter-spacing: 0;
    color: var(--ink-light);
  }
  .service-bar {
    position: absolute;
    left: 56px;
    top: 231px;
    width: 661px;
    height: 64px;
    background: var(--green);
  }
  .service-bar__text {
    position: absolute;
    left: 105px;
    top: 10px;
    font-weight: 700;
    font-size: 41px;
    line-height: 44px;
    letter-spacing: 3px;
    color: var(--ink-light);
  }
  .phone {
    position: absolute;
    left: 155px;
    top: 331px;
    font-weight: 700;
    font-size: 55px;
    line-height: 1;
    letter-spacing: 1px;
    color: var(--ink-light);
  }
  .status-band {
    position: absolute;
    left: 0;
    top: 429px;
    width: 1006px;
    height: 171px;
    background: var(--green);
    display: flex;
    align-items: center;
    justify-content: center;
  }
  .status-band__text {
    font-weight: 700;
    font-size: 156px;
    line-height: 1;
    letter-spacing: 3px;
    color: var(--ink-light);
    transform: translate(2px, 4px);
  }
  .website {
    position: absolute;
    left: 0;
    width: 1006px;
    top: 680px;
    text-align: center;
    font-weight: 600;
    font-size: 50px;
    line-height: 1;
    letter-spacing: 0;
    color: var(--ink-light);
  }
</style>
</head>
<body>
  <main class="canvas">
    <section class="board" aria-label="For sale board">
      <div class="brand-name">HAVEN</div>
      <div class="service-bar">
        <span class="service-bar__text">SALES &amp; LETTING</span>
      </div>
      <div class="phone">01 632 960418</div>
      <div class="status-band">
        <span class="status-band__text">FOR SALE</span>
      </div>
      <div class="website">WWW.HAVEN-ESTATES.CO.UK</div>
    </section>
  </main>
</body>
</html>
```